Bright Mesh Business Card

This is a business card for a printing company but I actually don't have a logo. Just need to typeset the words "Bright Mesh Printing" as the logo. Then add my name "Loretta Vance" + phone number + address

Target Market(s)

ceos and professionals

Industry/Entity Type

printing and manufacturing

Contact Information for Business Card

Bright Mesh Printing/ 4617 calloway st. S. El Monte, CA 91648/ 626-417-3980/ Loretta Vance

Font styles to use
Serif
Other font styles liked:
• a modern font would be nice

Colors
0054AA
0677BA
7BADD7
CADEEF
E8F1F8
0094D4
00A9DD
6FCCEA
C7EBF8
E9F6FB

Requirements
Must have
• company name, number, address
Nice to have
• nice bold feel
Should not have
• nothing in particular

```html
<!DOCTYPE html>
<html lang="en">
<head>
<meta charset="utf-8">
<title>Bright Mesh Printing – Business Card</title>
<link rel="stylesheet" href="https://fonts.googleapis.com/css2?family=Inter:wght@400;600;800&display=swap">
<style>
  :root {
    --page: #e4e4e4;
    --blue-top: #0b4696;
    --blue-bottom: #032a78;
    --brand-blue: #0d4a9c;
    --red: #ff0000;
    --white: #ffffff;
  }
  * { margin: 0; padding: 0; box-sizing: border-box; }
  html, body {
    width: 1200px; height: 1200px; overflow: hidden;
    background: var(--page);
    font-family: "Inter", Arial, sans-serif;
  }
  .card {
    position: absolute;
    left: 262px; width: 686px; height: 392px;
    border-radius: 22px; overflow: hidden;
  }
  .card--front { top: 165px; background: var(--white); }
  .card--back { top: 653px; background: var(--red); }
  .card__panel {
    position: absolute; left: 0; top: 0; bottom: 0; width: 335px;
    background: linear-gradient(180deg, var(--blue-top), var(--blue-bottom));
  }
  .contact {
    position: absolute; left: 52px; top: 112px;
    color: var(--white);
  }
  .contact__name { font-size: 22px; font-weight: 600; line-height: 1.1; }
  .contact__title { font-size: 16px; font-weight: 400; margin-top: 3px; }
  .contact__address { font-size: 15.5px; line-height: 1.25; margin-top: 16px; }
  .contact__list { list-style: none; margin-top: 18px; font-size: 15.5px; line-height: 1.25; }
  .contact__list li { display: flex; align-items: center; gap: 8px; }
  .contact__list svg { width: 12px; height: 12px; fill: var(--white); flex: none; }
  .brand {
    position: absolute; text-align: center;
    font-weight: 800; text-transform: uppercase; line-height: 1;
  }
  .brand__name { display: block; }
  .brand__sub { display: block; letter-spacing: 0.45em; margin-right: -0.45em; }
  .card--front .brand { left: 372px; width: 270px; top: 168px; color: var(--brand-blue); }
  .card--front .brand__name { font-size: 36px; letter-spacing: -0.02em; }
  .card--front .brand__sub { font-size: 15px; margin-top: 8px; }
  .card--back .brand { left: 0; right: 0; top: 148px; color: var(--white); }
  .card--back .brand__name { font-size: 56px; letter-spacing: -0.02em; }
  .card--back .brand__sub { font-size: 23px; margin-top: 10px; }
</style>
</head>
<body>
  <section class="card card--front" aria-label="Card front">
    <div class="card__panel" role="img" aria-label="Blue panel with a curved blue, white and red wave divider"></div>
    <div class="contact">
      <p class="contact__name">Loretta Vance</p>
      <p class="contact__title">President</p>
      <p class="contact__address">4617 Calloway St.<br>S. El Monte, CA 91648</p>
      <ul class="contact__list">
        <li><svg viewBox="0 0 24 24"><path d="M6.6 10.8c1.4 2.8 3.8 5.1 6.6 6.6l2.2-2.2c.3-.3.7-.4 1-.2 1.1.4 2.3.6 3.6.6.6 0 1 .4 1 1V20c0 .6-.4 1-1 1C10.6 21 3 13.4 3 4c0-.6.4-1 1-1h3.5c.6 0 1 .4 1 1 0 1.3.2 2.5.6 3.6.1.3 0 .7-.2 1z"/></svg>626-417-3980</li>
        <li><svg viewBox="0 0 24 24"><path d="M2 5h20v14H2z" fill="var(--white)"/><path d="M3.5 6.5 12 12.5l8.5-6" fill="none" stroke="var(--blue-bottom)" stroke-width="1.8"/></svg>info@brightmeshprinting.com</li>
        <li><svg viewBox="0 0 24 24"><circle cx="12" cy="12" r="10"/><path d="M2 12h20M12 2c3 3 3 17 0 20M12 2c-3 3-3 17 0 20" fill="none" stroke="var(--blue-bottom)" stroke-width="1.6"/></svg>brightmeshprinting.com</li>
      </ul>
    </div>
    <p class="brand"><span class="brand__name">Bright Mesh</span><span class="brand__sub">Printing</span></p>
  </section>

  <section class="card card--back" aria-label="Card back">
    <p class="brand"><span class="brand__name">Bright Mesh</span><span class="brand__sub">Printing</span></p>
  </section>
</body>
</html>
```